Bring my website out of the dark ages!

Website redesign for Velmar Consulting
www.velmarqx.com and www.trundlebox.ca
Currently dark (black), small font, boring, old
Want something simple, bright, fun, modern, clean and professional
Flexible content, any ideas appreciated
In business since 1998, focused on long term client relationships and being there when it matters.
Specialize solutions for clients based on their needs, vision and budget, not what the IT market thinks is the latest and greatest (and most profitable).
Want to eventually add helpful content (videos) and testimonials to the site for the benefit of the visitor

Target Market(s)

Anyone looking for IT services - target is a business with 25-100 employees.

Industry/Entity Type

It Company

Coding

Coded - Design and coding required

Number of Pages Required

4 page

Colors

Designer to choose colors to be used in the design.

Requirements
Must have
• Bright, clean, simple, no scrolling, fast
Nice to have
• Neat animation of some kind
Should not have
• scrolling
• too much information

```html
<!DOCTYPE html>
<html lang="en">
<head>
<meta charset="utf-8">
<title>Velmar Consulting — Your Partner in Technology Solutions</title>
<link rel="stylesheet" href="https://fonts.googleapis.com/css2?family=Poppins:wght@300;400&display=swap">
<style>
  :root {
    --sidebar-bg: #ffffff;
    --text-dark: #3a3a3a;
    --text-muted: #6f6f6f;
    --logo-grey: #8c8c8c;
    --accent: #f6a623;
    --rule: #d6d6d6;
    --circle-line: #cfcfcf;
    --hero-top: #9aa5b1;
    --hero-mid: #6c7a8a;
    --hero-bottom: #2e3a4b;
    --white: #ffffff;
  }
  * { box-sizing: border-box; margin: 0; padding: 0; }
  html, body { width: 1200px; height: 677px; overflow: hidden; }
  body { font-family: "Poppins", sans-serif; background: var(--sidebar-bg); position: relative; }

  .sidebar {
    position: absolute; left: 0; top: 0; width: 264px; height: 677px;
    background: var(--sidebar-bg);
  }
  .brand {
    position: absolute; left: 40px; top: 42px;
    font-weight: 300; font-size: 18px; color: var(--logo-grey); letter-spacing: 0.3px;
  }
  .brand-rule {
    position: absolute; left: 40px; top: 107px; width: 55px; height: 1px; background: var(--rule);
  }
  .main-nav { position: absolute; left: 40px; top: 136px; width: 178px; list-style: none; }
  .main-nav li {
    height: 70px; display: flex; align-items: center; justify-content: space-between;
    border-bottom: 1px dotted var(--rule);
    font-weight: 300; font-size: 18px; color: var(--text-dark); letter-spacing: 0.3px;
    padding-top: 0;
  }
  .main-nav li:last-child { border-bottom: none; }
  .main-nav li.is-active { color: var(--accent); }
  .chevron { width: 10px; height: 6px; margin-right: 4px; }

  .follow { position: absolute; left: 40px; top: 542px; }
  .follow-label { font-weight: 300; font-size: 14px; color: var(--text-muted); letter-spacing: 0.3px; }
  .social-links { display: flex; gap: 12px; margin-top: 14px; }
  .social-links span {
    width: 42px; height: 42px; border-radius: 50%;
    border: 2px solid var(--circle-line); display: block;
  }
  .social-links span.is-active { background: var(--accent); border-color: var(--accent); }

  .hero {
    position: absolute; left: 264px; top: 0; width: 936px; height: 677px;
    background:
      linear-gradient(180deg, rgba(46,58,75,0) 55%, rgba(46,58,75,0.6) 100%),
      linear-gradient(160deg, var(--hero-top) 0%, var(--hero-mid) 55%, var(--hero-bottom) 100%);
  }
  .hero-phone {
    position: absolute; right: 50px; top: 38px; display: flex; align-items: center; gap: 12px;
    color: var(--white); font-weight: 300; font-size: 22px; letter-spacing: 1.5px;
  }
  .hero-phone svg { width: 20px; height: 20px; }
  .hero-title {
    position: absolute; left: 0; right: 0; top: 285px; text-align: center;
    color: var(--white); font-weight: 300; font-size: 40px; line-height: 59px; letter-spacing: 2px;
  }
</style>
</head>
<body>
  <aside class="sidebar">
    <div class="brand">Velmar Consulting</div>
    <div class="brand-rule"></div>
    <ul class="main-nav">
      <li class="is-active">Home</li>
      <li>About Us</li>
      <li>Services
        <svg class="chevron" viewBox="0 0 10 6"><path d="M1 1l4 4 4-4" fill="none" stroke="#777" stroke-width="1.3"/></svg>
      </li>
      <li>Testimonials</li>
      <li>Contact Us</li>
    </ul>
    <div class="follow">
      <p class="follow-label">Follow Us On</p>
      <div class="social-links">
        <span aria-label="Social profile link"></span>
        <span aria-label="Social profile link"></span>
        <span class="is-active" aria-label="Social profile link"></span>
      </div>
    </div>
  </aside>

  <main class="hero" role="img" aria-label="Photo of two consultants working together at a laptop in a bright office">
    <div class="hero-phone">
      <svg viewBox="0 0 24 24"><path fill="#fff" d="M6.6 10.8c1.4 2.8 3.8 5.1 6.6 6.6l2.2-2.2c.3-.3.7-.4 1-.2 1.1.4 2.3.6 3.6.6.6 0 1 .4 1 1V20c0 .6-.4 1-1 1C10.6 21 3 13.4 3 4c0-.6.4-1 1-1h3.5c.6 0 1 .4 1 1 0 1.3.2 2.5.6 3.6.1.3 0 .7-.2 1l-2.3 2.2z"/></svg>
      555 014 2297
    </div>
    <h1 class="hero-title">Your Partner in<br>Technology Solutions</h1>
  </main>
</body>
</html>
```